Business card for Eyelash extension salon in Vellmont Hills,California USA

We need new business card for our salon in Vellmont Hills. The salon name is 'Lumarra' . We would like to have...Business name: Lumarra Name of person: will provide later Address 6128 N.Corbel Ridge Blvd Vellmont Hills , CA 90000 Phone: will provide later (Text only) Web: www.lumarrastudio-example.com Pictogrid icon, Friendvale icon follow us for seasonal campaign and news @lumarrastudioexample Design should look elegant, high-end, clean, simple, cohesive with my brand. Please refer my brand board. Business name color will be metallic bronzy color. Im thinking grey background or white background. Thanks

Target Market(s)

25-35. Gender neutral. People who are in Entertainment business industry.
This is High-end Eyelash extension salon in Vellmont Hills

Industry/Entity Type

Beauty Salon

Contact Information for Business Card

Business name: Lumarra
Name of person: will provide later
Address 6128 N.Corbel Ridge Blvd Vellmont Hills , CA 90000
Phone: will provide later (Text only)
Web: www.lumarrastudio-example.com
Pictogrid icon, Friendvale icon
follow us for seasonal campaign and news @lumarrastudioexample

Requirements
Must have
• Beautiful, elegant, clean and simple look but very attractive and modern
Should not have
• We don't like too clutter, too busy designs.

```html
<!DOCTYPE html>
<html lang="en">
<head>
<meta charset="utf-8">
<title>Lumarra Vellmont Hills – Business Card</title>
<link rel="stylesheet" href="https://fonts.googleapis.com/css2?family=Cabin:wght@400;500;600&family=Libre+Baskerville:wght@700&display=swap">
<style>
  :root {
    --paper: #ffffff;
    --band: #c8ad91;
    --bronze: #a8855a;
    --bronze-dark: #8a6a4f;
    --ink: #3a3a3c;
    --rule: #dedede;
    --gold-soft: #f6dfa0;
    --gold-fade: #fdf6e6;
  }
  html, body {
    margin: 0;
    padding: 0;
    width: 962px;
    height: 1200px;
    overflow: hidden;
    background: var(--paper);
    font-family: "Cabin", sans-serif;
  }
  .canvas { position: relative; width: 962px; height: 1200px; background: var(--paper); }
  .abs { position: absolute; }

  .confetti {
    position: absolute;
    left: 5px;
    right: 8px;
    background: linear-gradient(to bottom, var(--gold-soft) 0%, var(--gold-fade) 65%, rgba(255,255,255,0) 100%);
    opacity: 0.55;
  }
  .front .confetti { top: 0; height: 290px; }
  .back .confetti { top: 647px; height: 90px; }

  .wordmark {
    position: absolute;
    color: var(--bronze);
    font-weight: 400;
    letter-spacing: 2px;
    text-align: center;
    margin: 0;
    line-height: 1;
    white-space: nowrap;
  }
  .tagline {
    position: absolute;
    color: var(--bronze-dark);
    letter-spacing: 4px;
    margin: 0;
    line-height: 1;
    white-space: nowrap;
  }
  .front .wordmark { left: 0; width: 962px; top: 255px; font-size: 130px; }
  .front .tagline { left: 475px; top: 441px; font-size: 19px; }

  .band { position: absolute; left: 5px; width: 949px; background: var(--band); }
  .front .band { top: 531px; height: 35px; }

  .back .wordmark { left: 40px; width: 370px; top: 820px; font-size: 82px; }
  .back .tagline { left: 224px; top: 941px; font-size: 13px; letter-spacing: 3px; }

  .person-name {
    left: 474px; top: 756px; margin: 0;
    font-family: "Libre Baskerville", serif;
    font-size: 38px; color: var(--ink); line-height: 1;
  }
  .person-role { left: 476px; top: 805px; margin: 0; font-size: 23px; color: var(--bronze); line-height: 1.2; }
  .divider { left: 474px; top: 846px; width: 480px; height: 1px; background: var(--rule); }

  .contact { left: 474px; width: 480px; display: flex; align-items: flex-start; gap: 18px;
    color: var(--bronze-dark); font-weight: 600; font-size: 24px; line-height: 30px; }
  .contact svg { flex: none; width: 26px; height: 26px; margin-top: 2px; fill: var(--band); }
  .contact p { margin: 0; }
  .contact-address { top: 890px; }
  .contact-web { top: 991px; font-size: 23px; }
  .contact-phone { top: 1066px; }

  .social { left: 130px; width: 200px; top: 1042px; display: flex; justify-content: center; gap: 16px; }
  .social-name { display: flex; align-items: center; gap: 5px; font-size: 16px; font-weight: 500; color: var(--bronze-dark); }
  .social-name .dot { width: 10px; height: 10px; background: var(--band); }
  .handle { left: 90px; width: 280px; top: 1084px; text-align: center; font-size: 20px; color: var(--bronze-dark); margin: 0; }

  .back .band { top: 1162px; height: 38px; display: flex; align-items: center; justify-content: center;
    color: #fff; font-size: 21px; letter-spacing: 1px; }
</style>
</head>
<body>
<main class="canvas">
  <section class="front">
    <div class="confetti" role="img" aria-label="Scattered soft gold confetti dots"></div>
    <h1 class="wordmark">Lumarra</h1>
    <p class="tagline">VELLMONT HILLS</p>
    <div class="band"></div>
  </section>

  <section class="back">
    <div class="confetti" role="img" aria-label="Scattered soft gold confetti dots"></div>
    <p class="wordmark">Lumarra</p>
    <p class="tagline">VELLMONT HILLS</p>

    <div class="social abs">
      <span class="social-name"><span class="dot"></span>Friendvale</span>
      <span class="social-name"><span class="dot"></span>Pictogrid</span>
    </div>
    <p class="handle abs">@lumarrastudioexample</p>

    <h2 class="person-name abs">FULL NAME</h2>
    <p class="person-role abs">Manager</p>
    <div class="divider abs"></div>

    <div class="contact contact-address abs">
      <svg viewBox="0 0 24 24" aria-hidden="true"><path d="M12 1a8 8 0 0 0-8 8c0 6 8 14 8 14s8-8 8-14a8 8 0 0 0-8-8zm0 11a3 3 0 1 1 0-6 3 3 0 0 1 0 6z"/></svg>
      <p>6128 N.Corbel Ridge Blvd<br>Vellmont Hills , CA 90000</p>
    </div>
    <div class="contact contact-web abs">
      <svg viewBox="0 0 24 24" aria-hidden="true"><circle cx="12" cy="12" r="10" fill="none" stroke="#c8ad91" stroke-width="2"/><path d="M2 12h20M12 2c3 3 3 17 0 20M12 2c-3 3-3 17 0 20" fill="none" stroke="#c8ad91" stroke-width="1.6"/></svg>
      <p>www.lumarrastudio-example.com</p>
    </div>
    <div class="contact contact-phone abs">
      <svg viewBox="0 0 24 24" aria-hidden="true"><path d="M6.6 10.8a15 15 0 0 0 6.6 6.6l2.2-2.2c.3-.3.7-.4 1-.2 1.1.4 2.3.6 3.6.6.6 0 1 .4 1 1V20c0 .6-.4 1-1 1A17 17 0 0 1 3 4c0-.6.4-1 1-1h3.5c.6 0 1 .4 1 1 0 1.3.2 2.5.6 3.6.1.3 0 .7-.2 1z"/></svg>
      <p>(000) 000-0000</p>
    </div>

    <div class="band">- FOLLOW US FOR SEASONAL CAMPAIGN AND NEWS -</div>
  </section>
</main>
</body>
</html>
```